Wedding Photography business card

I need a business card made for a wedding photography business. Formal, unique, i like dark colors maybe black, white, gray, deep blue, silver. Sharp.

This is an idea i have i don't know if it would work.
Think Palm Beach, florida

work in mirror mode in your design program, Just an idea

Front side:
feminine, classy maybe white from wedding dress,
script, elegant,

back side:
masculine, black from tux, symbolizing strength, power,
serif

RV Photography
(555) 214-3097
www.ruthvlenses.example

Target Market(s)

upscale Weddings, targeting bride and groom

Industry/Entity Type

Wedding

Font styles to use
Serif
Script

Colors

Designer to choose colors to be used in the design.

Requirements
Must have
• both sides match somehow

```html
<!DOCTYPE html>
<html lang="en">
<head>
<meta charset="utf-8">
<title>RV Photography – Business Card, Design 3</title>
<link rel="stylesheet" href="https://fonts.googleapis.com/css2?family=Cormorant+Garamond:wght@400;500&family=Crimson+Text&family=Pinyon+Script&display=swap">
<style>
  :root {
    --page-bg: #ffffff;
    --label-grey: #8a8b8d;
    --title-ink: #111111;
    --card-border: #6d6e70;
    --brand-blue: #0070ba;
    --card-white: #ffffff;
    --contact-ink: #d6e6f4;
  }
  html, body {
    margin: 0;
    padding: 0;
    overflow: hidden;
    background: var(--page-bg);
  }
  .sheet {
    position: relative;
    width: 1000px;
    height: 1200px;
    overflow: hidden;
    background: var(--page-bg);
  }
  .sheet-title {
    position: absolute;
    top: 40px;
    left: 0;
    width: 1000px;
    margin: 0;
    text-align: center;
    font-family: "Crimson Text", serif;
    font-weight: 400;
    font-size: 38px;
    line-height: 1;
    color: var(--title-ink);
  }
  .side-label {
    position: absolute;
    left: 44px;
    margin: 0;
    font-family: "Crimson Text", serif;
    font-size: 38px;
    line-height: 1;
    color: var(--label-grey);
  }
  .side-label--front { top: 49px; }
  .side-label--back { top: 620px; }

  .card {
    position: absolute;
    box-sizing: border-box;
  }
  .card--front {
    left: 44px;
    top: 87px;
    width: 912px;
    height: 524px;
    border: 1px solid var(--card-border);
    background: var(--card-white);
  }
  .front-mark {
    position: absolute;
    left: 0;
    top: 234px;
    width: 100%;
    display: flex;
    align-items: center;
    justify-content: center;
    gap: 14px;
  }
  .front-mark-dot {
    width: 30px;
    height: 30px;
    border: 3px solid var(--brand-blue);
    border-radius: 50%;
    box-sizing: border-box;
  }
  .front-name {
    margin: 0;
    font-family: "Cormorant Garamond", serif;
    font-weight: 500;
    font-size: 40px;
    line-height: 56px;
    letter-spacing: 1px;
    color: var(--brand-blue);
  }
  .card--back {
    left: 46px;
    top: 660px;
    width: 907px;
    height: 521px;
    background: var(--brand-blue);
    text-align: center;
  }
  .back-name {
    position: absolute;
    top: 180px;
    left: 0;
    width: 100%;
    margin: 0;
    font-family: "Pinyon Script", cursive;
    font-weight: 400;
    font-size: 42px;
    line-height: 56px;
    color: var(--card-white);
  }
  .contact {
    position: absolute;
    top: 244px;
    left: 0;
    width: 100%;
    margin: 0;
    font-family: "Cormorant Garamond", serif;
    font-weight: 400;
    font-size: 24px;
    line-height: 29px;
    color: var(--contact-ink);
    font-style: normal;
  }
  .contact span { display: block; }
</style>
</head>
<body>
  <main class="sheet">
    <h1 class="sheet-title">Design-3</h1>

    <p class="side-label side-label--front">front</p>
    <section class="card card--front" aria-label="Card front">
      <div class="front-mark">
        <span class="front-mark-dot" aria-hidden="true"></span>
        <p class="front-name">RV Photography</p>
      </div>
    </section>

    <p class="side-label side-label--back">back</p>
    <section class="card card--back" aria-label="Card back">
      <h2 class="back-name">RV Photography</h2>
      <address class="contact">
        <span class="contact-phone">(555) 214-3097</span>
        <span class="contact-web">www.ruthvlenses.example</span>
      </address>
    </section>
  </main>
</body>
</html>
```